Business card design needed for rebranded top-end landscaping business

We need a new business card design, incorporating our logo (colours Green #8dc63f and Grey #8a8c8e) and also some options that include the colour dark navy (eg #000040) as our uniforms are navy with white and grey trim.

We are an innovative landscaping company that maintains high-end gardens for meticulous clients. We pride ourselves on our customer service, our professionalism, and our workmanship.

Our business name needs to be easily read and our branding needs to be bold and memorable, without screaming "tradesman"! We prefer clean lines over lots of fine detail.

The design MUST include:
- Business name ("Brambleton Gardenworks")
- Logo (file uploaded)
- Employee name
- Phone number
- Email address
- www.brambletongardenworks.com.au
- Facebook & Instagram logos
- The Turfcraft Guild logo (file uploaded) along with the word "Member"
- Licence "Lic. 618392K"

OPTIONAL inclusions:
- "Creating outdoor spaces for our community to be inspired, refreshed and re-energised"
- "Landscape Maintenance - Irrigation - Arboriculture" (dashes can be replaced with dots or other)
- "Fully qualified, licensed & insured"
- "Residential - Strata - Commercial - Real Estate" (dashes can be replaced with dots or other)

High-end professionals and retirees, real estate agents

Landscaping

See Project description

Sans Serif

Designer to choose colors to be used in the design.

• Must incorporate our logo, and colours Green #8dc63f and Grey #8a8c8e) from the logo, and the colour DARK NAVY (eg #000040).
• The design MUST include:
• - Business name ("Brambleton Gardenworks")
• - Logo (file uploaded)
• - Employee name
• - Phone number
• - Email address
• - www.brambletongardenworks.com.au
• - Facebook & Instagram logos
• - The Turfcraft Guild logo (file uploaded) along with the word "Member"
• - Licence "Lic. 618392K"
• OPTIONAL inclusions:
• - "Creating outdoor spaces for our community to be inspired, refreshed and re-energised"
• - "Landscape Maintenance - Irrigation - Arboriculture" (dashes can be replaced with dots or other)
• - "Fully qualified, licensed & insured"
• - "Residential - Strata - Commercial - Real Estate" (dashes can be replaced with dots or other)

```html
<!DOCTYPE html>
<html lang="en">
<head>
<meta charset="utf-8">
<title>Brambleton Gardenworks – Business Card</title>
<link href="https://fonts.googleapis.com/css2?family=Arimo:wght@400;700&display=swap" rel="stylesheet">
<style>
  :root {
    --stage: #8f8f8f;
    --green: #8dc63f;
    --green-deep: #4f9a1c;
    --green-bright: #9ed64a;
    --grey: #8a8c8e;
    --navy-dark: #000040;
    --navy-light: #0a0a7a;
    --white: #ffffff;
  }
  html, body {
    margin: 0;
    width: 1200px;
    height: 960px;
    overflow: hidden;
    background: var(--stage);
    font-family: "Arimo", Arial, sans-serif;
  }
  .card {
    position: absolute;
    width: 640px;
    height: 366px;
    border-radius: 26px;
    box-shadow: 0 10px 24px rgba(0,0,0,0.3);
    overflow: hidden;
  }
  /* Front */
  .card-front {
    left: 90px;
    top: 50px;
    background: var(--green-bright);
  }
  .member-badge {
    position: absolute;
    right: 40px;
    top: 30px;
    display: flex;
    flex-direction: column;
    align-items: center;
    gap: 6px;
  }
  .member-badge .badge-mark {
    width: 26px;
    height: 26px;
    border-radius: 50%;
    border: 2px solid var(--white);
    box-sizing: border-box;
  }
  .member-badge .badge-label {
    color: var(--white);
    font-size: 9px;
    letter-spacing: 3px;
  }
  .brand {
    display: flex;
    align-items: center;
    gap: 12px;
  }
  .brand-dot {
    border-radius: 50%;
    flex: none;
  }
  .brand-name {
    font-weight: 700;
    line-height: 1.05;
  }
  .card-front .brand {
    position: absolute;
    left: 0;
    right: 0;
    top: 120px;
    justify-content: center;
  }
  .card-front .brand-dot {
    width: 56px;
    height: 56px;
    background: var(--green-deep);
  }
  .card-front .brand-name {
    color: var(--green-deep);
    font-size: 36px;
  }
  .sectors {
    position: absolute;
    left: 0;
    right: 0;
    bottom: 40px;
    text-align: center;
    color: var(--white);
    font-size: 17px;
  }
  .sectors .sep {
    display: inline-block;
    width: 7px;
    height: 7px;
    border-radius: 50%;
    background: var(--white);
    margin: 0 10px;
    vertical-align: middle;
  }
  /* Back */
  .card-back {
    left: 470px;
    top: 540px;
    background: linear-gradient(110deg, var(--navy-dark) 0%, var(--navy-dark) 45%, var(--navy-light) 100%);
  }
  .social {
    position: absolute;
    right: 30px;
    top: 26px;
    display: flex;
    gap: 6px;
  }
  .social span {
    width: 20px;
    height: 20px;
    border-radius: 50%;
    background: var(--green);
  }
  .card-back .brand {
    position: absolute;
    left: 34px;
    top: 170px;
    width: 250px;
  }
  .card-back .brand-dot {
    width: 46px;
    height: 46px;
    background: var(--grey);
  }
  .card-back .brand-name {
    color: var(--green);
    font-size: 24px;
  }
  .divider {
    position: absolute;
    left: 300px;
    top: 110px;
    width: 1px;
    height: 170px;
    background: var(--grey);
  }
  .contact {
    position: absolute;
    left: 326px;
    top: 110px;
    color: var(--grey);
  }
  .contact .person {
    color: var(--green);
    font-weight: 700;
    font-size: 22px;
    margin: 0;
  }
  .contact .role {
    font-size: 15px;
    margin: 2px 0 16px;
  }
  .contact ul {
    list-style: none;
    margin: 0;
    padding: 0;
    font-size: 14px;
  }
  .contact li {
    display: flex;
    align-items: center;
    gap: 8px;
    margin-bottom: 6px;
  }
  .contact svg {
    width: 12px;
    height: 12px;
    fill: var(--green);
    flex: none;
  }
  .contact .licence {
    font-size: 15px;
    margin-top: 18px;
  }
</style>
</head>
<body>

<section class="card card-front">
  <div class="member-badge">
    <div class="badge-mark" role="img" aria-label="The Turfcraft Guild member badge"></div>
    <div class="badge-label">MEMBER</div>
  </div>
  <div class="brand">
    <span class="brand-dot"></span>
    <span class="brand-name">Brambleton Gardenworks</span>
  </div>
  <div class="sectors">
    Residential<span class="sep"></span>Strata<span class="sep"></span>Commercial<span class="sep"></span>Real Estate
  </div>
</section>

<section class="card card-back">
  <div class="social" aria-label="Social media links">
    <span></span><span></span>
  </div>
  <div class="brand">
    <span class="brand-dot"></span>
    <span class="brand-name">Brambleton Gardenworks</span>
  </div>
  <div class="divider"></div>
  <div class="contact">
    <p class="person">Daniel Harlow</p>
    <p class="role">President</p>
    <ul>
      <li>
        <svg viewBox="0 0 24 24"><path d="M6.6 10.8a15 15 0 0 0 6.6 6.6l2.2-2.2c.3-.3.7-.4 1-.2 1.1.4 2.3.6 3.6.6.6 0 1 .4 1 1V20c0 .6-.4 1-1 1A17 17 0 0 1 3 4c0-.6.4-1 1-1h3.5c.6 0 1 .4 1 1 0 1.3.2 2.5.6 3.6.1.3 0 .7-.2 1z"/></svg>
        369-480-2271
      </li>
      <li>
        <svg viewBox="0 0 24 24"><path d="M2 5h20v14H2z M2 5l10 8 10-8" /></svg>
        info@brambletongardenworks.com.au
      </li>
      <li>
        <svg viewBox="0 0 24 24"><circle cx="12" cy="12" r="10"/></svg>
        www.brambletongardenworks.com.au
      </li>
    </ul>
    <p class="licence">Lic. 618392K</p>
  </div>
</section>

</body>
</html>
```